KLT, Inc. business card desing

Design a business card for an contemporary e commerce company that sells fragrances and cosmetics. State of the art , high tech and super very fast delivery

Target Market(s)

e commerce customers like Bramble, Tolvex , and retailers wesites

Industry/Entity Type

Business

Contact Information for Business Card

On the Front :

scentharborline.example with some design element

On the back :
Dr. Marek Thornby
President

Phone ( icom) 555.207.6431
Cell (icon) 555.284.9062
Fax(icon) 555.613.4870
email (icon) marek@scentharborline.example

4815 Cedar Lane
Fernwick Bay 11990

Colors
b768aa
e667a6
abd036

Requirements
Must have
• all the above content info
Nice to have
• Could have and abstract perfume bottle
Should not have
• no faces, facial features,

```html
<!DOCTYPE html>
<html lang="en">
<head>
<meta charset="utf-8">
<title>Business card</title>
<link rel="stylesheet" href="https://fonts.googleapis.com/css2?family=Open+Sans:wght@400;600;700&display=swap">
<style>
  :root {
    --orchid: #b768aa;
    --orchid-deep: #8e3a84;
    --orchid-light: #d08ccb;
    --rose: #e667a6;
    --lime: #abd036;
    --paper: #ffffff;
    --backdrop: #ece8ec;
    --ink-soft: #9a6f95;
  }
  * { box-sizing: border-box; margin: 0; padding: 0; }
  html, body { width: 1200px; height: 913px; overflow: hidden; }
  body {
    background: var(--backdrop);
    font-family: "Open Sans", Arial, sans-serif;
    position: relative;
  }
  .card {
    position: absolute;
    top: 306px;
    width: 520px;
    height: 300px;
    border-radius: 18px;
    overflow: hidden;
    box-shadow: 0 6px 18px rgba(80, 40, 80, 0.18);
  }
  .card-front { left: 50px; background: var(--paper); }
  .card-back {
    left: 630px;
    background: linear-gradient(160deg, var(--orchid-light) 0%, var(--orchid) 45%, var(--orchid-deep) 100%);
  }
  .card-art { position: absolute; inset: 0; }

  .brand-name {
    position: absolute;
    left: 30px;
    top: 112px;
    font-size: 32px;
    font-weight: 600;
    letter-spacing: -0.5px;
    color: var(--rose);
  }
  .holder-name {
    position: absolute;
    right: 16px;
    top: 58px;
    font-size: 19px;
    font-weight: 700;
    color: var(--orchid);
  }
  .holder-title {
    position: absolute;
    right: 16px;
    top: 94px;
    font-size: 11px;
    color: var(--rose);
  }
  .rule { position: absolute; height: 1px; background: var(--orchid); }
  .rule-name { left: 250px; right: 16px; top: 88px; }
  .rule-contact { left: 30px; width: 300px; top: 196px; }

  .address {
    position: absolute;
    right: 16px;
    top: 118px;
    text-align: right;
    font-size: 12px;
    line-height: 18px;
    color: var(--ink-soft);
  }
  .contact-list {
    position: absolute;
    left: 30px;
    top: 206px;
    list-style: none;
    font-size: 13px;
    line-height: 19px;
    color: var(--rose);
  }
  .contact-list li { display: flex; align-items: center; gap: 7px; }
  .contact-list svg { width: 11px; height: 11px; fill: var(--rose); flex: none; }

  .ornament {
    position: absolute;
    left: 110px;
    top: 30px;
    width: 300px;
    height: 170px;
    border-radius: 50%;
    background: radial-gradient(ellipse at center, rgba(171,208,54,0.35) 0%, rgba(255,255,255,0.12) 45%, rgba(255,255,255,0) 72%);
  }
  .site-name {
    position: absolute;
    left: 0;
    right: 0;
    top: 212px;
    text-align: center;
    font-size: 30px;
    font-weight: 600;
    letter-spacing: -0.5px;
    color: var(--paper);
  }
</style>
</head>
<body>

<section class="card card-front" aria-label="Card front with contact details">
  <svg class="card-art" viewBox="0 0 520 300" aria-hidden="true">
    <path d="M520,170 C440,196 372,238 350,300 L402,300 C420,250 468,212 520,196 Z" fill="var(--orchid)"/>
    <path d="M520,162 C450,182 395,214 365,260" stroke="var(--orchid-light)" stroke-width="2" fill="none"/>
  </svg>

  <div class="brand-name">scentharborline</div>

  <div class="holder-name">Dr. Marek Thornby</div>
  <div class="rule rule-name"></div>
  <div class="holder-title">President</div>

  <div class="address">
    4815 Cedar Lane<br>
    Fernwick Bay 11990
  </div>

  <div class="rule rule-contact"></div>
  <ul class="contact-list">
    <li>
      <svg viewBox="0 0 24 24" aria-label="Phone"><path d="M6.6 10.8a15.1 15.1 0 0 0 6.6 6.6l2.2-2.2c.3-.3.7-.4 1-.2 1.1.4 2.3.6 3.6.6.6 0 1 .4 1 1V20c0 .6-.4 1-1 1A17 17 0 0 1 3 4c0-.6.4-1 1-1h3.5c.6 0 1 .4 1 1 0 1.3.2 2.5.6 3.6.1.3 0 .7-.2 1z"/></svg>
      555.207.6431
    </li>
    <li>
      <svg viewBox="0 0 24 24" aria-label="Cell"><path d="M7 1h10a2 2 0 0 1 2 2v18a2 2 0 0 1-2 2H7a2 2 0 0 1-2-2V3a2 2 0 0 1 2-2zm0 3v14h10V4zm5 15.5a1.2 1.2 0 1 0 0 2.4 1.2 1.2 0 0 0 0-2.4z"/></svg>
      555.284.9062
    </li>
    <li>
      <svg viewBox="0 0 24 24" aria-label="Fax"><path d="M6 2h12v6H6zM3 9h18a2 2 0 0 1 2 2v7h-4v4H5v-4H1v-7a2 2 0 0 1 2-2zm4 7v4h10v-4z"/></svg>
      555.613.4870
    </li>
    <li>
      <svg viewBox="0 0 24 24" aria-label="Email"><path d="M2 4h20a1 1 0 0 1 1 1v14a1 1 0 0 1-1 1H2a1 1 0 0 1-1-1V5a1 1 0 0 1 1-1zm1 2.5V18h18V6.5l-9 6z"/></svg>
      marek@scentharborline.example
    </li>
  </ul>
</section>

<section class="card card-back" aria-label="Card back with web address">
  <div class="ornament" role="img" aria-label="Soft decorative swirl ornament with a heart shape"></div>
  <div class="site-name">scentharborline.example</div>
</section>

</body>
</html>
```